Bright Lantern,

Tri-fold brochure. This brochure is designed to get attention from college students who wish to get hands-on broadcast and online experience and do so covering interesting stories and people in places traditional media does not go. I'll be their professor and adviser. Would like the brochure as a single fold using 8.5 X 11 although I would appreciate any suggestions on size or number of folds.

I'm interested in a design the designer is interested in. Love passion. You can see I have this brochure generally mapped out, but I am not stuck on photo placement. I don't care if a photo stretches 2 or 3 pages. I'm interested in other design elements besides my photos and copy.

I've included several photos that can be used. The only photo I'm stuck on is the Peter Vallory Building for the front page. It's a B&W page completely except for the Chicago flag at the bottom.

```html
<!DOCTYPE html>
<html lang="en">
<head>
<meta charset="utf-8">
<title>Tri-fold Brochure Inside Spread</title>
<link rel="stylesheet" href="https://fonts.googleapis.com/css2?family=Didact+Gothic&display=swap">
<style>
  :root {
    --backdrop: #d9d9d9;
    --paper: #f4f4f2;
    --ink: #1f1f1f;
    --ink-light: #ffffff;

    --blue-band: #1254ad;
    --blue-strip: #8ea9d6;
    --blue-panel: #cdd4e3;

    --red-band: #dc1c21;
    --red-strip: #efb59c;
    --red-panel: #f6e4dc;

    --green-band: #62821f;
    --green-strip: #c9cca3;
    --green-panel: #dddcca;
  }

  * { box-sizing: border-box; margin: 0; padding: 0; }

  html, body {
    width: 1200px;
    height: 864px;
    overflow: hidden;
    background: var(--backdrop);
  }

  .spread {
    position: absolute;
    left: 50px;
    top: 25px;
    width: 1100px;
    height: 814px;
    background: var(--paper);
    display: grid;
    grid-template-rows: 268px 268px 268px;
    row-gap: 5px;
    font-family: "Didact Gothic", sans-serif;
    color: var(--ink);
  }

  .row {
    display: grid;
    grid-template-columns: 550px 550px;
  }

  .page-half {
    display: grid;
    height: 100%;
    overflow: hidden;
  }
  .page-half.text-left  { grid-template-columns: 444px 8px 98px; }
  .page-half.text-right { grid-template-columns: 98px 8px 444px; }

  .copy {
    font-size: 12px;
    line-height: 14.6px;
    letter-spacing: 0.2px;
    padding-top: 34px;
  }
  .copy p + p { margin-top: 7px; }

  .text-left .copy {
    text-align: right;
    padding-right: 32px;
    padding-left: 92px;
  }
  .text-right .copy {
    text-align: left;
    padding-left: 32px;
    padding-right: 92px;
    padding-top: 40px;
  }

  .strip { position: relative; }
  .strip::before {
    content: "";
    position: absolute;
    top: 34px;
    width: 0; height: 0;
    border-top: 7px solid transparent;
    border-bottom: 7px solid transparent;
  }
  .text-left .strip::before  { right: 100%; border-right: 12px solid var(--strip-colour); }
  .text-right .strip::before { left: 100%;  border-left: 12px solid var(--strip-colour); }

  .band {
    display: flex;
    align-items: flex-start;
    justify-content: center;
    padding-top: 30px;
    color: var(--ink-light);
    font-size: 22px;
    line-height: 28px;
    letter-spacing: 0.5px;
    text-transform: uppercase;
    font-weight: 400;
    overflow: hidden;
  }
  .band .label {
    writing-mode: vertical-rl;
    white-space: nowrap;
  }

  .band.reads-up {
    align-items: flex-end;
    padding-top: 0;
    padding-bottom: 52px;
  }
  .band.reads-up .label { transform: rotate(180deg); }

  .section-blue  .copy  { background: var(--blue-panel); }
  .section-blue  .strip { background: var(--blue-strip); --strip-colour: var(--blue-strip); }
  .section-blue  .band  { background: var(--blue-band); }

  .section-red   .copy  { background: var(--red-panel); }
  .section-red   .strip { background: var(--red-strip); --strip-colour: var(--red-strip); }
  .section-red   .band  { background: var(--red-band); }

  .section-green .copy  { background: var(--green-panel); }
  .section-green .strip { background: var(--green-strip); --strip-colour: var(--green-strip); }
  .section-green .band  { background: var(--green-band); }

  .photo { height: 100%; }
  .photo-platform {
    background: linear-gradient(100deg, #5a4a48 0%, #3f4356 35%, #6b6a70 60%, #8b8784 80%, #4e4c4f 100%);
  }
  .photo-trumpeter {
    background: radial-gradient(ellipse at 85% 30%, #c99a58 0%, #7a4a22 35%, transparent 60%),
                linear-gradient(100deg, #8a5a2a 0%, #3a2414 35%, #1a120d 60%, #6e4420 100%);
  }
  .photo-camera-crew {
    background: linear-gradient(100deg, #5c6148 0%, #8a8a6e 25%, #2a2a2e 55%, #4c5060 80%, #36373d 100%);
  }
</style>
</head>
<body>
  <main class="spread">

    <section class="row">
      <div class="page-half text-left section-blue">
        <div class="copy">
          <p>Lorem ipsum dolor rehent qui officipsam quiae dusda si doluptae int et etur. Dion rent et volupti idunt officint et is doluptasimi, sitasperest remos di cone sus molor sequibus duciat voluptatis delit eaquis dignit acias alit dolore adi sequae re sum fugia volectat.</p>
          <p>Ebit quias anti aut es ad et atius, cuptas aut ullore nisi nuscium nat officae stibusam inctur? Ugitem vel mi, cusam, to illuptam, es ius dolessimus corem quas nos a dolor ecipitas ipsum volore.</p>
          <p>Videlig nimaximus himil mo qui corestr untiuntis rem et exeritas ex exceate mporumquamus commo volupta tatur. Endunti comnimp orunto quo excepuda nus.</p>
        </div>
        <div class="strip"></div>
        <h2 class="band"><span class="label">Small Town<br>Chicago Defined</span></h2>
      </div>
      <div class="photo photo-platform" role="img" aria-label="Commuters crowding a city train platform beside an elevated train"></div>
    </section>

    <section class="row">
      <div class="photo photo-trumpeter" role="img" aria-label="Street musician in a hat playing trumpet under warm holiday lights"></div>
      <div class="page-half text-right section-red">
        <h2 class="band reads-up"><span class="label">Social Media</span></h2>
        <div class="strip"></div>
        <div class="copy">
          <p>Lorem ipsum dolor rehent qui officipsam quiae dusda si doluptae int et etur. Dion rent et volupti idunt officint et is doluptasimi, sitasperest remos di cone sus molor sequibus duciat voluptatis delit eaquis dignit acias alit dolore adi sequae re sum fugia volectat.</p>
          <p>Ebit quias anti aut es ad et atius, cuptas aut ullore nisi nuscium nat officae stibusam inctur? Ugitem vel mi, cusam, to illuptam, es ius dolessimus corem quas nos a dolor ecipitas ipsum volore.</p>
          <p>Videlig nimaximus himil mo qui corestr untiuntis rem et exeritas ex exceate mporumquamus commo volupta tatur. Endunti comnimp orunto quo excepuda nus.</p>
        </div>
      </div>
    </section>

    <section class="row">
      <div class="page-half text-left section-green">
        <div class="copy">
          <p>Lorem ipsum dolor rehent qui officipsam quiae dusda si doluptae int et etur. Dion rent et volupti idunt officint et is doluptasimi, sitasperest remos di cone sus molor sequibus duciat voluptatis delit eaquis dignit acias alit dolore adi sequae re sum fugia volectat.</p>
          <p>Ebit quias anti aut es ad et atius, cuptas aut ullore nisi nuscium nat officae stibusam inctur? Ugitem vel mi, cusam, to illuptam, es ius dolessimus corem quas nos a dolor ecipitas ipsum volore.</p>
          <p>Videlig nimaximus himil mo qui corestr untiuntis rem et exeritas ex exceate mporumquamus commo volupta tatur. Endunti comnimp orunto quo excepuda nus exerae nem quiam que atur.</p>
        </div>
        <div class="strip"></div>
        <h2 class="band"><span class="label">Taped On<br>Location</span></h2>
      </div>
      <div class="photo photo-camera-crew" role="img" aria-label="Student video crew filming with a camcorder on a busy city sidewalk"></div>
    </section>

  </main>
</body>
</html>
```